Poster design for the MIRUM VELUM magic show.

We need a poster design for our magic show. This isn't your typical 'small town' magic show. Our show features world class magicians from the Wonder Lantern, in Hollywood California. The show is geared toward everyone, it is family friendly - with a little bit of an edge. We want people to see the poster and feel like they are going to have a unique and sophisticated magical experience. We also want individuals and couples to see the poster and feel like it is a show for them and not only for children.
Updates

Target Market(s)

WBC audience, family audience, the age range is anywhere from 5 - 105. Cool people.

Industry/Entity Type

Town

Requirements
Must have
• Our attached .jpg of the magician floating in the air. Poster size 24x36"
Must have text:
The 3rd Annual Albuquerque Conjuring Revue Presents (small type)
Mirum Velum (should be larger type)
November 24th - 25th
Showtimes 3:00PM & 7:30PM Saturday, 2:00PM Sunday
Tickets available at www.ZelaraSeats.example For more information contact Zelara Theatre @ 505.241.9067
Nice to have
• A sort of old school/antique feeling to the poster.
Perhaps a theater marquee
Check out www.tundravelvet.example - we love the feeling of this site for our poster...
Feel free to adjust the provided .jpg accordingly in regards to color/size/interaction with the rest of the poster
Should not have
• Should not have clowns, bunnies, anything that would make it feel like a 3 year old's magic themed birthday party.

```html
<!DOCTYPE html>
<html lang="en">
<head>
<meta charset="utf-8">
<title>Mirum Velum — Poster</title>
<link rel="stylesheet" href="https://fonts.googleapis.com/css2?family=Zilla+Slab:wght@500;600;700&display=swap">
<style>
  :root {
    --magenta: #a52380;
    --ink: #ffffff;
    --veil: rgba(255, 255, 255, 0.82);
  }
  html, body {
    margin: 0;
    padding: 0;
    width: 800px;
    height: 1200px;
    overflow: hidden;
    background: var(--magenta);
  }
  .poster {
    position: relative;
    width: 800px;
    height: 1200px;
    background: var(--magenta);
    color: var(--ink);
    font-family: "Zilla Slab", Georgia, serif;
    overflow: hidden;
  }
  .presenter {
    position: absolute;
    left: 70px;
    top: 50px;
    margin: 0;
    font-size: 27px;
    font-weight: 700;
    letter-spacing: 0.2px;
  }
  .title {
    position: absolute;
    left: 62px;
    top: 78px;
    margin: 0;
    font-size: 166px;
    line-height: 136px;
    font-weight: 600;
    letter-spacing: 2px;
  }
  .title span { display: block; }
  .dates {
    position: absolute;
    left: 70px;
    top: 388px;
    margin: 0;
    font-size: 56px;
    font-weight: 700;
    letter-spacing: 0.5px;
  }
  .dates sup {
    font-size: 24px;
    vertical-align: 26px;
    margin-left: 2px;
  }
  .showtimes {
    position: absolute;
    left: 70px;
    top: 492px;
  }
  .showtimes-label {
    margin: 0 0 6px 0;
    font-size: 22px;
    font-weight: 700;
    letter-spacing: 0.3px;
  }
  .showtime-row {
    display: flex;
    align-items: baseline;
    margin: 0;
    height: 48px;
  }
  .day {
    width: 214px;
    font-size: 42px;
    font-weight: 700;
  }
  .time {
    font-size: 28px;
    font-weight: 700;
  }
  .time small {
    font-size: 10px;
    font-weight: 700;
  }
  .levitation-art {
    position: absolute;
    left: 0;
    top: 625px;
    width: 800px;
    height: 410px;
    background:
      radial-gradient(ellipse 55% 38% at 55% 48%, var(--veil), rgba(255,255,255,0.25) 70%, rgba(255,255,255,0) 100%);
  }
  .tickets {
    position: absolute;
    left: 70px;
    top: 1092px;
    margin: 0;
    font-size: 21px;
    font-weight: 700;
    line-height: 31px;
    letter-spacing: 0.2px;
  }
</style>
</head>
<body>
  <main class="poster">
    <p class="presenter">The 3rd Annual Albuquerque Conjuring Revue Presents</p>
    <h1 class="title"><span>MIRUM</span><span>VELUM</span></h1>
    <p class="dates">NOVEMBER 24<sup>TH</sup> - 25<sup>TH</sup></p>

    <section class="showtimes">
      <p class="showtimes-label">SHOWTIMES:</p>
      <p class="showtime-row"><span class="day">Saturday</span><span class="time">3:00<small>PM</small> &amp; 7:30<small>PM</small></span></p>
      <p class="showtime-row"><span class="day">Sunday</span><span class="time">2:00<small>PM</small></span></p>
    </section>

    <div class="levitation-art" role="img" aria-label="White silhouette illustration of a magician floating horizontally in the air"></div>

    <p class="tickets">Tickets available at www.ZelaraSeats.example<br>For more information contact Zelara Theatre: 505.241.9067</p>
  </main>
</body>
</html>
```